The Velvet Lintel with an elephant incorporated in the background

Target Market(s)

Real estate

Industry/Entity Type

Real Estate

Contact Information for Business Card

On back on want my name & number
In front I want the business name, "the velvet lintel", below to say staging & design

Logo Text

The Velvet Lintel

Font styles to use
Serif

Colors
000000

Requirements
Must have
• I want an elephant behind the writing in gold transperant

```html
<!DOCTYPE html>
<html lang="en">
<head>
<meta charset="utf-8">
<title>The Velvet Lintel — Business Cards</title>
<link rel="stylesheet" href="https://fonts.googleapis.com/css2?family=Josefin+Sans:wght@300;400&family=Montserrat:wght@700&family=Open+Sans:wght@400&display=swap">
<style>
  :root {
    --backdrop: #3b3531;
    --card: #0e0e0e;
    --gold: #e2b21c;
    --gold-line: rgba(226, 178, 28, 0.55);
    --grey-line: rgba(255, 255, 255, 0.22);
    --muted: #8c8c8c;
    --white: #f2f2f2;
  }
  * { margin: 0; padding: 0; box-sizing: border-box; }
  html, body { width: 1200px; height: 900px; overflow: hidden; }
  body {
    background: var(--backdrop);
    display: flex;
    align-items: center;
    justify-content: center;
    gap: 50px;
  }
  .card {
    position: relative;
    width: 520px;
    height: 300px;
    background: var(--card);
    border-radius: 3px;
    box-shadow: 0 14px 30px rgba(0, 0, 0, 0.45);
    overflow: hidden;
  }

  /* Back card: contact side */
  .card-back .brand-mark {
    position: absolute;
    left: 0;
    top: 0;
    width: 235px;
    height: 100%;
    display: flex;
    flex-direction: column;
    align-items: center;
    justify-content: center;
    gap: 18px;
  }
  .brand-dot {
    width: 70px;
    height: 70px;
    border-radius: 50%;
    background: var(--gold);
  }
  .brand-name {
    font-family: "Josefin Sans", sans-serif;
    font-weight: 400;
    color: var(--gold);
    text-transform: uppercase;
    letter-spacing: 1px;
    text-align: center;
    font-size: 21px;
    line-height: 1.2;
  }
  .card-back .divider {
    position: absolute;
    left: 245px;
    top: 60px;
    width: 1px;
    height: 180px;
    background: var(--gold-line);
  }
  .elephant-watermark {
    position: absolute;
    left: 270px;
    top: 30px;
    width: 210px;
    height: 270px;
    border-radius: 45% 50% 0 0;
    background: radial-gradient(ellipse at 50% 45%, rgba(226, 178, 28, 0.16), rgba(226, 178, 28, 0.04) 70%, transparent);
  }
  .contact {
    position: absolute;
    left: 270px;
    top: 88px;
    font-family: "Open Sans", sans-serif;
    color: var(--white);
    font-size: 13.5px;
    line-height: 1.45;
  }
  .contact .person {
    font-family: "Montserrat", sans-serif;
    font-weight: 700;
    color: var(--gold);
    font-size: 17px;
    text-transform: uppercase;
    margin-bottom: 10px;
  }
  .contact .line {
    display: flex;
    align-items: center;
    gap: 7px;
  }
  .contact .line svg { width: 11px; height: 11px; fill: var(--gold); flex: none; }
  .contact .address { margin-top: 10px; }

  /* Front card: brand side */
  .card-front {
    display: flex;
    flex-direction: column;
    align-items: center;
    justify-content: center;
  }
  .card-front .brand-dot { width: 60px; height: 60px; margin-bottom: 14px; }
  .card-front .rule { width: 290px; height: 1px; background: var(--grey-line); }
  .card-front .brand-name {
    font-weight: 300;
    font-size: 30px;
    letter-spacing: 1.5px;
    margin: 10px 0 4px;
  }
  .tagline {
    font-family: "Josefin Sans", sans-serif;
    font-weight: 300;
    color: var(--muted);
    text-transform: uppercase;
    letter-spacing: 2px;
    font-size: 11px;
    margin-bottom: 8px;
  }
</style>
</head>
<body>

  <section class="card card-back">
    <div class="brand-mark">
      <div class="brand-dot"></div>
      <div class="brand-name">The Velvet Lintel</div>
    </div>
    <div class="divider"></div>
    <div class="elephant-watermark" role="img" aria-label="Faint gold elephant silhouette in the background"></div>
    <div class="contact">
      <p class="person">Marcus Hale</p>
      <p class="line">
        <svg viewBox="0 0 24 24" aria-hidden="true"><path d="M6.6 10.8a15.1 15.1 0 0 0 6.6 6.6l2.2-2.2a1 1 0 0 1 1-.25 11.4 11.4 0 0 0 3.6.57 1 1 0 0 1 1 1V20a1 1 0 0 1-1 1A17 17 0 0 1 3 4a1 1 0 0 1 1-1h3.5a1 1 0 0 1 1 1c0 1.25.2 2.45.57 3.57a1 1 0 0 1-.25 1z"/></svg>
        (044)555014827
      </p>
      <p class="line">
        <svg viewBox="0 0 24 24" aria-hidden="true"><path d="M2 5h20v14H2z M2 5l10 8 10-8" /></svg>
        hello@velvetlintel.com
      </p>
      <p class="address">78, Harrow Lane Court,<br>Eastmere, 40215</p>
    </div>
  </section>

  <section class="card card-front">
    <div class="brand-dot"></div>
    <div class="rule"></div>
    <div class="brand-name">The Velvet Lintel</div>
    <div class="tagline">Staging &amp; Design</div>
    <div class="rule"></div>
  </section>

</body>
</html>
```